Dravolith Business Card

I have a logo that I would like to use to design the Business Card for Dravolith Construction LLC. We are a commercial general contractor in San Antonio Texas. Id like a simple and sleek design. Message me if you have any questions. Thanks

Industry/Entity Type

Contractor

```html
<!DOCTYPE html>
<html lang="en">
<head>
<meta charset="utf-8">
<title>Dravolith Business Card</title>
<link href="https://fonts.googleapis.com/css2?family=Montserrat:wght@500;700&family=Oswald:wght@500;600&display=swap" rel="stylesheet">
<style>
  :root {
    --blue: #3a6fbd;
    --charcoal: #2f3033;
    --white: #ffffff;
    --ink: #2b2c2f;
    --stage: #dcdddf;
    --muted: #d8dbe2;
  }
  * { box-sizing: border-box; margin: 0; padding: 0; }
  html, body {
    width: 1200px; height: 974px; overflow: hidden;
    background: var(--stage);
    font-family: "Montserrat", Arial, sans-serif;
  }
  .card {
    position: absolute; left: 220px; width: 760px; height: 434px;
    overflow: hidden; box-shadow: 0 8px 24px rgba(0,0,0,.18);
  }
  .card--back { top: 36px; }
  .card--front { top: 504px; }
  .card__shapes { position: absolute; inset: 0; }
  .brand {
    position: absolute; display: flex; align-items: center; gap: 14px;
    color: var(--ink); font-weight: 700; line-height: 1;
  }
  .brand__mark { width: 44px; height: 44px; background: var(--blue); flex: none; }
  .brand__name { font-size: 30px; letter-spacing: 1px; }
  .brand__sub { font-size: 14px; letter-spacing: 2.4px; margin-top: 6px; }
  .card--back .brand { left: 48px; top: 88px; }
  .card--front .brand { left: 150px; top: 52px; }
  .website {
    position: absolute; left: 48px; bottom: 40px;
    color: var(--white); font-size: 15px; font-weight: 500; letter-spacing: .5px;
  }
  .holder { position: absolute; left: 48px; bottom: 70px; color: var(--white); }
  .holder__name {
    font-family: "Oswald", Arial, sans-serif; font-weight: 600;
    font-size: 50px; letter-spacing: 2px; line-height: 1;
  }
  .holder__role { font-size: 18px; font-weight: 500; letter-spacing: 3px; margin-top: 8px; }
  .contacts {
    position: absolute; right: 34px; top: 130px; list-style: none;
    color: var(--white); font-size: 13px; font-weight: 500; text-align: right;
  }
  .contacts li {
    display: flex; justify-content: flex-end; align-items: center;
    gap: 10px; height: 24px;
  }
  .contacts svg { width: 14px; height: 14px; flex: none; }
</style>
</head>
<body>

<section class="card card--back" aria-label="Card back">
  <svg class="card__shapes" viewBox="0 0 760 434" preserveAspectRatio="none">
    <rect width="760" height="434" fill="var(--blue)"/>
    <polygon points="0,0 420,0 320,210 0,250" fill="var(--white)"/>
    <polygon points="0,250 320,210 760,210 760,434 0,434" fill="var(--charcoal)"/>
  </svg>
  <div class="brand">
    <span class="brand__mark"></span>
    <div>
      <div class="brand__name">DRAVOLITH</div>
      <div class="brand__sub">CONSTRUCTION LLC</div>
    </div>
  </div>
  <p class="website">www.dravolithbuild.com</p>
</section>

<section class="card card--front" aria-label="Card front">
  <svg class="card__shapes" viewBox="0 0 760 434" preserveAspectRatio="none">
    <rect width="760" height="434" fill="var(--charcoal)"/>
    <polygon points="0,0 560,0 470,190 0,160" fill="var(--white)"/>
    <polygon points="0,160 470,190 560,434 0,434" fill="var(--blue)"/>
  </svg>
  <div class="brand">
    <span class="brand__mark"></span>
    <div>
      <div class="brand__name">DRAVOLITH</div>
      <div class="brand__sub">CONSTRUCTION LLC</div>
    </div>
  </div>
  <ul class="contacts">
    <li>412 Alamo Quarry Road
      <svg viewBox="0 0 14 14"><path d="M7 1a4 4 0 0 1 4 4c0 3-4 8-4 8S3 8 3 5a4 4 0 0 1 4-4z" fill="var(--blue)"/><circle cx="7" cy="5" r="1.4" fill="var(--charcoal)"/></svg>
    </li>
    <li>Suite 3, San Antonio TX
      <svg viewBox="0 0 14 14"><rect x="2" y="2" width="10" height="10" fill="none" stroke="var(--blue)" stroke-width="1.6"/></svg>
    </li>
    <li>014 275 3816
      <svg viewBox="0 0 14 14"><rect x="4" y="1" width="6" height="12" rx="1.2" fill="var(--blue)"/></svg>
    </li>
    <li>014 275 3816
      <svg viewBox="0 0 14 14"><path d="M3 1.5l2.5 0 1 3-1.6 1.2a7 7 0 0 0 3.4 3.4L9.5 7.5l3 1v2.5c0 .8-.7 1.5-1.5 1.5C6 12.5 1.5 8 1.5 3c0-.8.7-1.5 1.5-1.5z" fill="var(--blue)"/></svg>
    </li>
    <li>office@dravolithbuild.com
      <svg viewBox="0 0 14 14"><rect x="1" y="3" width="12" height="8" fill="var(--blue)"/><path d="M1 3l6 5 6-5" fill="none" stroke="var(--charcoal)" stroke-width="1.2"/></svg>
    </li>
    <li>www.dravolithbuild.com
      <svg viewBox="0 0 14 14"><circle cx="7" cy="7" r="5.5" fill="none" stroke="var(--blue)" stroke-width="1.4"/><path d="M1.5 7h11M7 1.5c2.5 3 2.5 8 0 11M7 1.5c-2.5 3-2.5 8 0 11" fill="none" stroke="var(--blue)" stroke-width="1"/></svg>
    </li>
  </ul>
  <div class="holder">
    <div class="holder__name">MARA ELLISON</div>
    <div class="holder__role">GENERAL MANAGER</div>
  </div>
</section>

</body>
</html>
```